Harbor Petroleum Business Cards

I would like to design some options for about 10 sets of double sided business cards for our team with a raised logo with a Silver glossy finished logo. We are a privately funded upstream Oil & Gas producer drilling vertical wells in Central Oklahoma with a long term production (ROI driven) strategy that we implement through an annual drilling program. We are focused on a shallow / vertical / long life / low decline strategy. We are based in downtown Tulsa Oklahoma. I have attached a sample business card and a picture of our hallway logo which we would like to replicate on the business cards.

Target Market(s)

SEC Accredited Investors and other Oil & Gas Operators

Industry/Entity Type

Upstream Oil & Gas

Contact Information for Business Card

You can see the sample photo attached, but email / website / address / direct phone / Cell Phone / Name / Title / Fax

Font styles to use
Other font styles liked:
• Felix Titling

Colors
0054AA
0677BA
7BADD7
CADEEF
E8F1F8

Requirements
Must have
• Glossy raised logo
Nice to have
• Possibly a new logo.
Should not have
• No Greens /

```html
<!DOCTYPE html>
<html lang="en">
<head>
<meta charset="utf-8">
<title>Harbor Petroleum Business Cards</title>
<link href="https://fonts.googleapis.com/css2?family=Tinos:ital,wght@0,400;0,700;1,700&display=swap" rel="stylesheet">
<style>
  :root {
    --backdrop: #e4e5e7;
    --card: #ffffff;
    --ink-dark: #3a3a3a;
    --ink-mid: #5c5c5c;
    --ink-soft: #6e6e6e;
    --icon: #7a7a7a;
    --mark: #8a8a8a;
  }
  * { margin: 0; padding: 0; box-sizing: border-box; }
  html, body {
    width: 1200px; height: 1200px; overflow: hidden;
    background: var(--backdrop);
    font-family: "Tinos", "Times New Roman", serif;
  }
  .card {
    position: absolute;
    left: 172px; width: 856px; height: 500px;
    background: var(--card);
    box-shadow: 0 2px 6px rgba(0,0,0,0.18);
  }
  .card--front { top: 82px; }
  .card--back { top: 616px; }

  .company-name {
    position: absolute;
    color: var(--ink-dark);
    font-weight: 400;
    text-transform: uppercase;
    letter-spacing: 0.5px;
    white-space: nowrap;
  }
  .card--front .company-name { left: 55px; top: 172px; font-size: 23px; }

  .person-name {
    position: absolute; left: 55px; top: 209px;
    font-size: 28px; color: var(--ink-mid); letter-spacing: 0.3px;
  }
  .job-title {
    position: absolute; right: 50px; top: 275px;
    text-align: right; font-style: italic; font-weight: 700;
    font-size: 19px; line-height: 28px; color: var(--ink-soft);
  }
  .contact-list {
    position: absolute; list-style: none;
    font-size: 20px; color: var(--ink-soft);
  }
  .contact-list li {
    display: flex; align-items: center; height: 36px; gap: 14px;
  }
  .contact-list--phones { left: 55px; top: 355px; }
  .contact-list--web { right: 52px; top: 355px; text-align: right; }
  .contact-list--web li { justify-content: flex-end; }
  .contact-icon { width: 16px; height: 16px; fill: var(--icon); flex: none; }

  .brand-lockup {
    position: absolute; left: 0; right: 0; top: 180px;
    display: flex; flex-direction: column; align-items: center; gap: 22px;
  }
  .brand-dot {
    width: 74px; height: 74px; border-radius: 50%; background: var(--mark);
  }
  .card--back .company-name { position: static; font-size: 32px; }
</style>
</head>
<body>
  <section class="card card--front">
    <div class="company-name">Harbor Petroleum, LLC</div>
    <div class="person-name">Dorian K. Vasquell, CPL</div>
    <div class="job-title">Executive Vice President<br>Land, LEgal &amp; Business Development</div>

    <ul class="contact-list contact-list--phones">
      <li>
        <svg class="contact-icon" viewBox="0 0 16 16" aria-hidden="true"><path d="M3.5 1.5l2.3 2.6-1.3 1.6c.9 2 2.4 3.5 4.3 4.4l1.6-1.3 2.6 2.3-1.3 2.2C6.6 13 3 9.4 1.3 4.3z"/></svg>
        <span>539-555-0142</span>
      </li>
      <li>
        <svg class="contact-icon" viewBox="0 0 16 16" aria-hidden="true"><path d="M4.5 1h7v14h-7zM5.7 2.5v10h4.6v-10z"/><circle cx="8" cy="13.7" r=".6"/></svg>
        <span>918-555-0187</span>
      </li>
      <li>
        <svg class="contact-icon" viewBox="0 0 16 16" aria-hidden="true"><path d="M4 2h8v4H4zM2 7h12v6h-2v-2H4v2H2zM5 12h6v3H5z"/></svg>
        <span>918-555-0163</span>
      </li>
    </ul>

    <ul class="contact-list contact-list--web">
      <li>
        <span>DKV@HPTulsa.com</span>
        <svg class="contact-icon" viewBox="0 0 16 16" aria-hidden="true"><path d="M1 4h14v9H1zM1.5 4.5L8 9l6.5-4.5v1.2L8 10.2 1.5 5.7z"/></svg>
      </li>
      <li>
        <span>www.HarborPetroleumLLC.com</span>
        <svg class="contact-icon" viewBox="0 0 16 16" aria-hidden="true"><path d="M8 1a7 7 0 100 14A7 7 0 008 1zm0 1.4c.8 1 1.3 2.3 1.5 3.6h-3C6.7 4.7 7.2 3.4 8 2.4zM2.5 7.3h3.9c0 .5 0 1 .1 1.4H2.5a5.6 5.6 0 010-1.4zm7 0h4a5.6 5.6 0 010 1.4h-4zM6.5 10h3c-.2 1.3-.7 2.6-1.5 3.6-.8-1-1.3-2.3-1.5-3.6z"/></svg>
      </li>
      <li>
        <span>22 North Elm Ave., Suite 900 Tulsa, OK 74103</span>
        <svg class="contact-icon" viewBox="0 0 16 16" aria-hidden="true"><path d="M8 1a4.5 4.5 0 00-4.5 4.5C3.5 9 8 13 8 13s4.5-4 4.5-7.5A4.5 4.5 0 008 1zm0 6.3a1.8 1.8 0 110-3.6 1.8 1.8 0 010 3.6zM3 14h10v1.2H3z"/></svg>
      </li>
    </ul>
  </section>

  <section class="card card--back">
    <div class="brand-lockup">
      <div class="brand-dot"></div>
      <div class="company-name">Harbor Petroleum, LLC</div>
    </div>
  </section>
</body>
</html>
```